Best Seller Cover Design for Inspirational Non-Fiction, Self-Help Book

I've been working diligently on a book title "Quietly Charted Harbor" that will be pivotal for my coaching business. We're heavily investing in marketing and public relations for this and would love it to be a best seller (every other's dream). I need an amazing book cover design that is eye-catching, description, creative, interesting, and compelling, Can you work your magic?I've attached a detailed description along with the content for the back cover. Please let me know if all the content does not fit and I'm happy to reduce it. I need a cover that sells and speaks to the description, whatever you think that will be best. Book DetailsTitle: Self-Defined SuccessSubtitle: Spoiler Alert: You Already Have Everything It TakesAuthor: Rilka T. NguyenSpecifics:- The book will be 5.5" by 8.5" and 216 pages (may change slightly and we can update the spine in final revisions). - Paperback and leave space for a bar code- Will need the raw files so this can be redesigned into hardcover down the line- Bookvale book cover upload ready- Final file will also need the front cover only for e-book version- Add profile headshot (attached) to back-cover if space permits.I do not have a clear vision of what will be best for this cover but I really like the evocative style of Oswin Tarkell Plentiful book. Thank you!

Target Market(s)

Professionals in transition, aspiring or new entrepreneurs, change-makers.

Font styles to use
Serif
Script

Colors

Designer to choose colors to be used in the design.

Requirements
Must have
• Traditional but with elements that make it interesting and provocative since it is speaking to a twist on a topic that has been well talked about, success.

```html
<!DOCTYPE html>
<html lang="en">
<head>
<meta charset="utf-8">
<title>Quietly Charted Harbor — Cover Spread</title>
<link href="https://fonts.googleapis.com/css2?family=Barlow+Condensed:wght@600;700&family=Libre+Baskerville:wght@700&family=Quicksand:wght@400;500;600&display=swap" rel="stylesheet">
<style>
  :root {
    --paper-light: #f4f2f3;
    --paper-mid: #e4dfe1;
    --paper-shadow: #cfc8cb;
    --accent-red: #e0141b;
    --ink: #1d1d1d;
    --tab-white: #ffffff;
    --guide-line: #bdb8ba;
  }
  html, body { margin: 0; padding: 0; overflow: hidden; }
  body { width: 1200px; height: 854px; }
  .cover-spread {
    position: relative;
    width: 1200px;
    height: 854px;
    overflow: hidden;
    background:
      radial-gradient(ellipse at 20% 30%, rgba(255,255,255,.7), transparent 55%),
      radial-gradient(ellipse at 80% 75%, rgba(255,255,255,.6), transparent 50%),
      radial-gradient(ellipse at 55% 10%, rgba(200,190,195,.35), transparent 45%),
      linear-gradient(135deg, var(--paper-light), var(--paper-mid) 50%, var(--paper-light));
    font-family: "Quicksand", sans-serif;
    color: var(--ink);
  }
  .paper-texture { position: absolute; inset: 0; }
  .trim-guide {
    position: absolute;
    border: 1px solid var(--guide-line);
    opacity: .7;
  }
  .trim-back { left: 33px; top: 8px; width: 538px; height: 828px; border-right: none; }
  .trim-spine { left: 571px; top: 8px; width: 66px; height: 828px; }
  .trim-front { left: 637px; top: 8px; width: 534px; height: 828px; border-left: none; }

  /* Back cover */
  .back-copy {
    position: absolute;
    left: 82px;
    top: 80px;
    width: 450px;
    font-size: 12.4px;
    line-height: 16.5px;
    font-weight: 500;
  }
  .back-copy p { margin: 0 0 16.5px; }
  .back-hook { color: var(--accent-red); font-style: italic; font-weight: 600; }
  .back-heading { color: var(--accent-red); font-weight: 600; }

  /* Spine */
  .spine-tab { position: absolute; left: 582px; top: 52px; }
  .spine-author {
    position: absolute;
    left: 600px;
    top: 106px;
    transform: translate(-50%, -50%) rotate(90deg);
    font-family: "Barlow Condensed", sans-serif;
    font-weight: 700;
    font-size: 13px;
    white-space: nowrap;
  }
  .spine-title {
    position: absolute;
    left: 606px;
    top: 449px;
    transform: translate(-50%, -50%) rotate(-90deg);
    font-family: "Barlow Condensed", sans-serif;
    font-weight: 700;
    font-size: 28px;
    letter-spacing: .5px;
    color: var(--accent-red);
    white-space: nowrap;
  }

  /* Front cover */
  .torn-window { position: absolute; left: 0; top: 0; }
  .front-title {
    position: absolute;
    left: 768px;
    top: 190px;
    margin: 0;
    font-family: "Barlow Condensed", sans-serif;
    font-weight: 700;
    font-size: 82px;
    line-height: 74px;
    letter-spacing: 1.5px;
    color: var(--accent-red);
  }
  .front-subtitle {
    position: absolute;
    left: 730px;
    top: 452px;
    width: 320px;
    margin: 0;
    text-align: center;
    font-family: "Libre Baskerville", serif;
    font-weight: 700;
    font-size: 16.5px;
    line-height: 25px;
  }
  .author-tab { position: absolute; left: 815px; top: 758px; }
  .front-author {
    position: absolute;
    left: 818px;
    top: 768px;
    width: 160px;
    text-align: center;
    font-family: "Barlow Condensed", sans-serif;
    font-weight: 700;
    font-size: 21px;
    line-height: 26px;
  }
</style>
</head>
<body>
<main class="cover-spread">
  <div class="paper-texture" role="img" aria-label="Crumpled white paper texture across the whole spread"></div>

  <div class="trim-guide trim-back"></div>
  <div class="trim-guide trim-spine"></div>
  <div class="trim-guide trim-front"></div>

  <section class="back-copy">
    <p class="back-hook">When all is said and done, what will matter to you most?</p>
    <p>Following someone else's path or society's definition of "success" doesn't often lead to personal fulfillment. At the end of the day, we genuinely want to succeed—not live a life defined by others.</p>
    <p>You can achieve anything you desire, and when you aim high for your spark of passion you will succeed. Passion is what awakens the heart, fires the soul, and fills the spirit. It is passion that energizes and sparks the pull forward through all barriers, uncertainty, and challenges.</p>
    <p>On this journey, we are asked to turn inward and search for the invisible, the hidden, and the sacred possibilities in order to claim what is ours in truth. We will then fill that shell with a desire that will ignite its creation.</p>
    <p>May this book serve as your guide on how to evoke this clarity and desire for your most authentic path enabling you to create a vision for your future that will bring you the ultimate sense of fulfillment. In addition, this book will show you the steps to navigate the path forward toward this new dream giving you the opportunity to awaken innate abilities you didn't know you had that will open the door to success.</p>
    <p class="back-heading">About the Author:</p>
    <p>Rilka T. Varsome has built her platform of a vision-driven life after 10 years of experience working as a business strategy advisor in Meridian 500 companies and at Halvern &amp; Pryce. Combining her advisory experience with her passion for spiritual principles of success, she now empowers entrepreneurs, change-makers, and leaders to step into their truth and bring their unique vision to life. Enabling them to change their lives, revolutionize their work, create greater impact in the world.</p>
  </section>

  <svg class="spine-tab" width="38" height="108" viewBox="0 0 38 108" aria-hidden="true">
    <polygon points="4,6 14,8 18,0 24,6 34,4 36,30 32,60 35,100 22,104 12,108 3,100 6,70 2,40" fill="var(--tab-white)"/>
  </svg>
  <div class="spine-author">RILKA T.</div>
  <div class="spine-title">QUIETLY CHARTED HARBOR</div>

  <svg class="torn-window" width="1200" height="854" viewBox="0 0 1200 854" aria-hidden="true">
    <polygon points="745,170 836,153 877,116 943,141 1067,153 1097,207 1121,331 1101,389 1084,463 1092,530 993,571 819,563 720,550 703,513 712,414 695,281 728,240"
      fill="var(--paper-shadow)" transform="translate(4,5)" opacity=".6"/>
    <polygon points="745,170 836,153 877,116 943,141 1067,153 1097,207 1121,331 1101,389 1084,463 1092,530 993,571 819,563 720,550 703,513 712,414 695,281 728,240"
      fill="var(--tab-white)"/>
  </svg>
  <h1 class="front-title">QUIETLY<br>CHARTED<br>HARBOR</h1>
  <p class="front-subtitle">Fair Warning: The Map Was<br>Folded In Your Pocket</p>

  <svg class="author-tab" width="168" height="48" viewBox="0 0 168 48" aria-hidden="true">
    <polygon points="8,6 40,2 90,8 140,3 160,10 168,24 158,40 110,44 60,40 20,46 4,36 0,20" fill="var(--tab-white)"/>
  </svg>
  <div class="front-author">RILKA T.</div>
</main>
</body>
</html>
```